Share the Sound referal Postcard Design

"Share the Sound" friends and family referral program for an audiology (hearing aid) clinic. We go for a boutique, professional, elite look rather than cheap hearing aid images (our providers are all doctors). Website is www.larkvalehearing.com. The final design should be eye catching but professional with a call to action at the bottom. Here is some sample verbiage that we were considering... "Your friend ____________ just experience Fuller Days through Finer Listening at Larkvale Hearing Center and would like you to have the same amazing experience! Please call LVHC at 582-9137 for a FREE hearing screening and consultation with one of our Doctors. Bring this postcard for an additional $250 discount if further treatment is recommended. "
Target Market(s)
Seniors, middle age, affluent hearing aid potential users
Industry/Entity Type
Boutique
Requirements
Must have
- Contact information for the clinic, brief description of the program, call to action
Should not have
- Smiley old people :)

```html
<!DOCTYPE html>
<html lang="en">
<head>
<meta charset="utf-8">
<title>Share the Sound – Referral Postcard</title>
<link href="https://fonts.googleapis.com/css2?family=Open+Sans:wght@400;600;700&family=Questrial&display=swap" rel="stylesheet">
<style>
  :root {
    --navy: #203f7f;
    --navy-deep: #1b356c;
    --rule-grey: #9ea3ab;
    --ink: #2b2b2b;
    --muted: #8a8a8a;
    --paper: #ffffff;
    --backdrop: #e9e6e1;
  }
  * { box-sizing: border-box; margin: 0; padding: 0; }
  html, body { width: 1200px; height: 1000px; overflow: hidden; }
  body {
    background: var(--backdrop);
    font-family: "Open Sans", sans-serif;
    color: var(--ink);
    position: relative;
  }
  .postcard {
    position: absolute;
    left: 260px;
    width: 680px;
    height: 453px;
    background: var(--paper);
    box-shadow: 0 4px 14px rgba(0,0,0,.18);
    overflow: hidden;
  }
  /* ---------- front ---------- */
  .postcard--front { top: 30px; }
  .front__top-band { position: absolute; left: 0; top: 0; width: 100%; height: 16px; background: var(--navy); }
  .front__portrait {
    position: absolute; left: 0; top: 16px; width: 100%; height: 318px;
    background: radial-gradient(ellipse at 50% 35%, #8fa3ad 0%, #5f7782 45%, #3c4a52 100%);
  }
  .front__rule { position: absolute; left: 0; top: 334px; width: 100%; height: 7px; background: var(--navy); }
  .front__rule-grey { position: absolute; left: 0; top: 341px; width: 100%; height: 4px; background: var(--rule-grey); }
  .front__offices {
    position: absolute; left: 22px; top: 356px; display: flex;
    font-family: "Questrial", sans-serif;
  }
  .office {
    width: 148px; padding: 0 12px; text-align: right;
    font-size: 10.5px; line-height: 1.35; color: #4a4a4a;
    border-right: 1px solid var(--navy);
  }
  .office:first-child { padding-left: 0; }
  .office:last-child { border-right: none; text-align: left; }
  .office__name {
    font-family: "Open Sans", sans-serif; font-weight: 700;
    font-size: 10.5px; color: var(--navy); text-transform: uppercase;
  }
  .front__brand { position: absolute; right: 22px; top: 356px; text-align: center; }
  .brand-name { font-family: "Open Sans", sans-serif; font-weight: 700; font-size: 17px; color: var(--navy); line-height: 1.1; }
  .brand-url { font-weight: 700; font-size: 10px; color: var(--navy); margin-top: 4px; }
  .front__bottom-bar {
    position: absolute; left: 0; bottom: 0; width: 100%; height: 36px;
    background: var(--navy-deep); color: #fff; font-weight: 600;
    font-size: 14px; padding: 9px 0 0 22px;
  }
  .front__bottom-bar strong { font-weight: 700; font-size: 12px; }
  /* ---------- back ---------- */
  .postcard--back { top: 513px; }
  .back__message { position: absolute; left: 34px; top: 30px; width: 300px; }
  .back__title { font-weight: 700; font-size: 27px; letter-spacing: .3px; color: #1d1d1d; text-align: center; margin-bottom: 6px; }
  .back__body { font-size: 16.5px; line-height: 1.35; color: #333; }
  .back__body + .back__body { margin-top: 16px; }
  .blank { display: inline-block; width: 100px; border-bottom: 1px solid #333; }
  .back__divider { position: absolute; left: 360px; top: 40px; height: 360px; border-left: 1px dotted #aaa; }
  .back__stamp {
    position: absolute; right: 34px; top: 70px; width: 94px; height: 100px;
    border: 2px solid #a9a9a9; color: #a9a9a9; font-size: 15px;
    display: flex; align-items: center; justify-content: center;
  }
  .back__address-lines { position: absolute; left: 392px; top: 200px; width: 252px; }
  .back__address-lines span { display: block; height: 38px; border-bottom: 1px solid #777; }
  .back__stripes { position: absolute; right: 0; bottom: 28px; width: 300px; }
  .back__stripes .thick { height: 12px; background: var(--navy); }
  .back__stripes .thin { height: 4px; background: var(--navy); margin-top: 5px; }
</style>
</head>
<body>
  <section class="postcard postcard--front">
    <div class="front__top-band"></div>
    <div class="front__portrait" role="img" aria-label="Studio portrait of the three clinic doctors against a soft blue-grey backdrop"></div>
    <div class="front__rule"></div>
    <div class="front__rule-grey"></div>
    <div class="front__offices">
      <div class="office">
        <div class="office__name">Ashford Office</div>
        412 N. Maple St.<br>Ashford, WA 99001<br>(555) 582-9137
      </div>
      <div class="office">
        <div class="office__name">Pinecrest Office</div>
        88 Harlow St.<br>Pinecrest, WA 99002<br>(555) 431-2760
      </div>
      <div class="office">
        <div class="office__name">Brookhaven Office</div>
        270 South Third Ave.<br>Brookhaven, WA 99003<br>(555) 764-3318
      </div>
    </div>
    <div class="front__brand">
      <div class="brand-name">Larkvale Hearing Center</div>
      <div class="brand-url">www.larkvalehearing.com</div>
    </div>
    <div class="front__bottom-bar">Toll Free: <strong>582-9137</strong></div>
  </section>

  <section class="postcard postcard--back">
    <div class="back__message">
      <h1 class="back__title">SHARE THE SOUND</h1>
      <p class="back__body">Your friend <span class="blank"></span> just experience Fuller Days through Finer Listening at Larkvale Hearing Center and would like you to have the same amazing experience!</p>
      <p class="back__body">Please call LVHC at 582-9137 for a FREE hearing screening and consultation with one of our Doctors.</p>
    </div>
    <div class="back__divider"></div>
    <div class="back__stamp">POSTAL</div>
    <div class="back__address-lines"><span></span><span></span><span></span><span></span><span></span><span></span></div>
    <div class="back__stripes"><div class="thick"></div><div class="thin"></div></div>
  </section>
</body>
</html>
```